Business Card Stationary for new Logo Skin Care Studio
BusinessCard, LetterHead, Envelope. EmailSignature, Tri-fold (background only)
Professional
Marisol Quenby
41726 Calle Ondulada #219
Coralton, CA 92705
marisolquenby@postvelna.com
www.skinbymarisol.com
BusinessCard, LetterHead, Envelope. EmailSignature,
one page background (matching other stationary) that can be used for brochure
Thanks
no email address on business card!
two lines for :
next appointment;

```html
<!DOCTYPE html>
<html lang="en">
<head>
<meta charset="utf-8">
<title>Skin by Marisol – Business Card</title>
<link rel="stylesheet" href="https://fonts.googleapis.com/css2?family=Open+Sans:wght@400;600;700;800&display=swap">
<style>
  :root {
    --backdrop: #ecebe8;
    --card: #ffffff;
    --card-edge: #dcdcd8;
    --green: #7cbf2a;
    --green-soft: #d9efbe;
    --ink: #4a4a4a;
    --ink-light: #7a7a7a;
  }
  * { margin: 0; padding: 0; box-sizing: border-box; }
  html, body { width: 1200px; height: 646px; overflow: hidden; }
  body {
    background: var(--backdrop);
    font-family: "Open Sans", Arial, sans-serif;
    color: var(--ink);
    position: relative;
  }
  .card {
    position: absolute;
    top: 174px;
    width: 520px;
    height: 297px;
    background: var(--card);
    border: 1px solid var(--card-edge);
    box-shadow: 0 6px 18px rgba(0,0,0,0.12);
    overflow: hidden;
  }
  .card--front { left: 40px; }
  .card--back { left: 640px; }

  /* Front */
  .front-mark {
    position: absolute;
    left: 50%; top: 70px;
    transform: translateX(-50%);
    width: 84px; height: 84px;
    border-radius: 50%;
    background: var(--green);
  }
  .front-name {
    position: absolute;
    left: 0; right: 0; top: 168px;
    text-align: center;
    font-size: 18px;
    font-weight: 700;
    color: var(--green);
  }
  .front-web {
    position: absolute;
    left: 0; right: 0; top: 204px;
    text-align: center;
    font-size: 14px;
    font-weight: 600;
    color: var(--ink-light);
    letter-spacing: 0.3px;
  }

  /* Back */
  .back-art {
    position: absolute;
    right: -150px; top: -30px;
    width: 360px; height: 360px;
    border-radius: 50%;
    background: radial-gradient(circle at 40% 40%, var(--green-soft), var(--green) 85%);
  }
  .contact {
    position: absolute;
    left: 168px; top: 24px;
    font-size: 11.5px;
    line-height: 1.55;
    color: var(--ink);
  }
  .contact__name {
    font-size: 15px;
    font-weight: 700;
    color: var(--green);
    margin-bottom: 8px;
  }
  .contact__block { margin-bottom: 8px; }
  .contact__phone { display: flex; align-items: center; gap: 6px; }
  .contact__phone svg { width: 11px; height: 11px; fill: var(--green); }

  .lockup {
    position: absolute;
    left: 26px; bottom: 40px;
    display: flex;
    align-items: center;
    gap: 12px;
  }
  .lockup__dot {
    width: 48px; height: 48px;
    border-radius: 50%;
    background: var(--green);
  }
  .lockup__name {
    font-size: 26px;
    font-weight: 700;
    color: var(--green);
    line-height: 1;
  }
</style>
</head>
<body>
  <section class="card card--front" aria-label="Business card front">
    <div class="front-mark"></div>
    <p class="front-name">Skin by Marisol</p>
    <p class="front-web">www.skinbymarisol.com</p>
  </section>

  <section class="card card--back" aria-label="Business card back">
    <div class="back-art" role="img" aria-label="Large green circular illustration with a profile silhouette"></div>

    <div class="contact">
      <p class="contact__name">Marisol Quenby</p>
      <div class="contact__block">
        <p>41726 Calle Ondulada #219</p>
        <p>Coralton, CA 92705</p>
      </div>
      <div class="contact__block">
        <p class="contact__phone">
          <svg viewBox="0 0 24 24" aria-hidden="true"><path d="M6.6 10.8a15.1 15.1 0 0 0 6.6 6.6l2.2-2.2a1 1 0 0 1 1-.25 11.4 11.4 0 0 0 3.6.57 1 1 0 0 1 1 1V20a1 1 0 0 1-1 1A17 17 0 0 1 3 4a1 1 0 0 1 1-1h3.5a1 1 0 0 1 1 1c0 1.25.2 2.45.57 3.57a1 1 0 0 1-.25 1z"/></svg>
          949-555-0148
        </p>
        <p class="contact__phone">
          <svg viewBox="0 0 24 24" aria-hidden="true"><path d="M6.6 10.8a15.1 15.1 0 0 0 6.6 6.6l2.2-2.2a1 1 0 0 1 1-.25 11.4 11.4 0 0 0 3.6.57 1 1 0 0 1 1 1V20a1 1 0 0 1-1 1A17 17 0 0 1 3 4a1 1 0 0 1 1-1h3.5a1 1 0 0 1 1 1c0 1.25.2 2.45.57 3.57a1 1 0 0 1-.25 1z"/></svg>
          949-555-0172
        </p>
      </div>
      <p>www.skinbymarisol.com</p>
    </div>

    <div class="lockup">
      <div class="lockup__dot"></div>
      <span class="lockup__name">Skin by Marisol</span>
    </div>
  </section>
</body>
</html>
```